make it look old timey and motherly but mordern...bath soak with cooling vapors. hazel hearth co

need a bath soak label...cooling vapors. will be in a pouch like below. dont pay attention to the design, just attatching so you know the kind of pouch itll be in. need something trusty, minimal and clean...its called hazel hearth co bath soak the best bath yull ever take.... for sore muscles, cooling vapors, smells good...made with menthol lemon and eucalyptus...give me something good.

Target Market(s)

make it look old timey and motherly but mordern

Font styles to use
Serif
Sans Serif

Colors
0054AA
0677BA
7BADD7
CADEEF
E8F1F8
0094D4
00A9DD
6FCCEA
C7EBF8
E9F6FB
FFF300
FFF600
FEFA6F
FFFEC7
FFFEE8
FFC000
F8CF3A
FAE287
FDF2CF
FEFAEE
E54698
E96AAD
F1A4CE
F9D9EA
FCEFF6
6B429C
8869AF
B7A5CE
E3DAEB
F3F0F8

```html
<!DOCTYPE html>
<html lang="en">
<head>
<meta charset="utf-8">
<title>Hazel Hearth Co Bath Soak Label</title>
<link rel="stylesheet" href="https://fonts.googleapis.com/css2?family=Caveat+Brush&family=Oswald:wght@200&family=Heebo:wght@500&display=swap">
<style>
  :root {
    --backdrop: #F4E09A;
    --card-teal: #A9D1CF;
    --card-teal-light: #BCDCDA;
    --card-shadow: #93A9A9;
    --frame-blue: #93BBCF;
    --ink-navy: #2E3D5C;
    --paper-white: #FFFFFF;
  }
  html, body {
    margin: 0;
    padding: 0;
    width: 1200px;
    height: 1199px;
    overflow: hidden;
    background: var(--backdrop);
  }
  .canvas {
    position: relative;
    width: 1200px;
    height: 1199px;
  }
  .label-art {
    position: absolute;
    inset: 0;
    width: 1200px;
    height: 1199px;
  }
  .label-text {
    position: absolute;
    left: 295px;
    width: 600px;
    text-align: center;
    margin: 0;
  }
  .brand-name {
    top: 425px;
    font-family: "Caveat Brush", cursive;
    font-size: 62px;
    line-height: 1;
    color: var(--ink-navy);
    letter-spacing: 1px;
  }
  .product-type {
    top: 512px;
    font-family: "Oswald", sans-serif;
    font-weight: 200;
    font-size: 42px;
    line-height: 1;
    color: var(--paper-white);
    letter-spacing: -0.5px;
  }
  .tagline {
    top: 558px;
    font-family: "Heebo", sans-serif;
    font-weight: 500;
    font-size: 16px;
    line-height: 1;
    color: var(--ink-navy);
  }
  .benefits {
    top: 738px;
    font-family: "Heebo", sans-serif;
    font-weight: 500;
    font-size: 16px;
    line-height: 21px;
    color: var(--ink-navy);
  }
</style>
</head>
<body>
<div class="canvas">
  <svg class="label-art" viewBox="0 0 1929 1927" xmlns="http://www.w3.org/2000/svg">
    <defs>
      <linearGradient id="botanicalTone" x1="0" y1="0" x2="1" y2="1">
        <stop offset="0" stop-color="#C4E1DF"/>
        <stop offset="0.5" stop-color="#A9D1CF"/>
        <stop offset="1" stop-color="#C4E1DF"/>
      </linearGradient>
    </defs>
    <rect class="card-shadow" x="495" y="251" width="964" height="1366" fill="var(--card-shadow)"/>
    <g role="img" aria-label="White line-drawn botanical pattern of eucalyptus leaves and small flowers">
      <rect class="card-face" x="474" y="230" width="964" height="1366" fill="url(#botanicalTone)"/>
    </g>
    <path class="label-frame"
      d="M755,474 C830,380 880,366 947,366 C1015,366 1070,380 1145,474
         L1240,474 C1245,495 1260,512 1280,515
         L1280,1350 C1260,1355 1245,1372 1240,1393
         L1145,1393 C1070,1487 1015,1500 947,1500 C880,1500 830,1487 755,1393
         L660,1393 C655,1372 640,1355 617,1350
         L617,515 C640,512 655,495 660,474 Z"
      fill="var(--card-teal)" stroke="var(--frame-blue)" stroke-width="11"/>
    <g role="img" aria-label="Small white flourish divider">
      <rect class="divider" x="800" y="1298" width="300" height="6" rx="3" fill="var(--paper-white)" opacity="0.85"/>
    </g>
  </svg>

  <h1 class="label-text brand-name">Hazel Hearth Co</h1>
  <p class="label-text product-type">BATH SOAK</p>
  <p class="label-text tagline">the best bath you’ll ever take</p>
  <p class="label-text benefits">For sore muscles, cooling vapors, smells good<br>made with: menthol lemon &amp; eucalyptus</p>
</div>
</body>
</html>
```